Shine Barn Auto Care Business Card

2 side business card design for an auto detailing business

Target Market(s)

Auto detailing

Contact Information for Business Card

Things included

The business name “Shine Barn Auto Care”
Owen Marchetti
(403)871-2964
Ridgeview, Sk

Services offered - complete interior& exterior detail
- paint correction & protection
- ceramic coating
- trim restore
- auto carpet & seat cleaning

Requirements
Must have
• Colours that are in my logo

Services offered

My name Owen Marchetti
403-871-2964
Ridgeview, Sk

Not too sure in what order for these ?
Website. Shinebarnautocare.com
Instagram Shinebarnautocare
Email. Shinebarnautoac@mailbox-example.com

```html
<!DOCTYPE html>
<html lang="en">
<head>
<meta charset="utf-8">
<title>Shine Barn Auto Care – Business Card</title>
<link rel="stylesheet" href="https://fonts.googleapis.com/css2?family=Montserrat:wght@400;500;700&family=Michroma&display=swap">
<style>
  :root {
    --backdrop: #575757;
    --card-white: #ffffff;
    --card-black: #1e1e1e;
    --brand-red: #a00f12;
    --ink: #1b1b1b;
    --muted: #555555;
    --light: #f2f2f2;
  }
  * { box-sizing: border-box; margin: 0; padding: 0; }
  html, body { width: 1200px; height: 800px; overflow: hidden; }
  body {
    background: var(--backdrop);
    font-family: "Montserrat", sans-serif;
    display: flex;
    align-items: center;
    justify-content: center;
    gap: 40px;
  }
  .card {
    position: relative;
    width: 540px;
    height: 309px;
    border-radius: 18px;
    border-bottom: 3px solid var(--brand-red);
    box-shadow: 0 14px 30px rgba(0,0,0,.35);
    overflow: hidden;
  }
  .card--front { background: var(--card-white); }
  .card--back { background: var(--card-black); }

  /* front: brand block */
  .brand {
    position: absolute;
    top: 50px;
    right: 50px;
    display: flex;
    align-items: center;
    gap: 16px;
  }
  .brand__mark { width: 62px; height: 62px; flex: none; }
  .brand__name {
    font-family: "Michroma", sans-serif;
    color: var(--ink);
    font-size: 20px;
    line-height: 1.25;
    letter-spacing: 1px;
  }
  .front__web {
    position: absolute;
    right: 50px;
    top: 128px;
    color: var(--brand-red);
    font-size: 12px;
    letter-spacing: .5px;
  }

  /* front: contact block */
  .contact {
    position: absolute;
    left: 44px;
    bottom: 32px;
  }
  .contact__name {
    font-family: "Michroma", sans-serif;
    font-weight: 400;
    color: var(--brand-red);
    font-size: 19px;
    letter-spacing: 1px;
    margin-bottom: 12px;
  }
  .contact__row {
    display: flex;
    align-items: center;
    gap: 10px;
    color: var(--muted);
    font-size: 13px;
    line-height: 21px;
  }
  .contact__icon { width: 11px; height: 11px; fill: var(--brand-red); flex: none; }

  /* back */
  .back__brand {
    position: absolute;
    top: 30px;
    left: 50%;
    transform: translateX(-50%);
    display: flex;
    flex-direction: column;
    align-items: center;
    gap: 8px;
  }
  .back__mark { width: 104px; height: 104px; }
  .back__name {
    font-weight: 700;
    color: var(--brand-red);
    font-size: 13px;
    letter-spacing: 2px;
    white-space: nowrap;
  }
  .services {
    position: absolute;
    left: 0; right: 0;
    bottom: 40px;
    text-align: center;
  }
  .services__title {
    color: var(--brand-red);
    font-weight: 700;
    font-size: 14px;
    letter-spacing: .5px;
    margin-bottom: 6px;
  }
  .services__line {
    color: var(--light);
    font-size: 14px;
    font-weight: 500;
    line-height: 21px;
  }
  .services__dot { color: var(--brand-red); margin: 0 6px; }
</style>
</head>
<body>

  <section class="card card--front" aria-label="Business card front">
    <div class="brand">
      <svg class="brand__mark" viewBox="0 0 62 62" aria-hidden="true">
        <circle cx="31" cy="31" r="27" fill="none" stroke="var(--brand-red)" stroke-width="5"/>
      </svg>
      <div class="brand__name">SHINE BARN<br>AUTO CARE</div>
    </div>
    <p class="front__web">www.ShineBarn.com</p>

    <div class="contact">
      <h1 class="contact__name">OWEN MARCHETTI</h1>
      <p class="contact__row">
        <svg class="contact__icon" viewBox="0 0 12 12" aria-hidden="true"><path d="M6 0a4 4 0 0 0-4 4c0 3 4 8 4 8s4-5 4-8a4 4 0 0 0-4-4zm0 5.6A1.6 1.6 0 1 1 6 2.4a1.6 1.6 0 0 1 0 3.2z"/></svg>
        Ridgeview, Sk
      </p>
      <p class="contact__row">
        <svg class="contact__icon" viewBox="0 0 12 12" aria-hidden="true"><path d="M2.4 0.5l2 2.4-1.2 1.3c.8 1.7 2 2.9 3.6 3.6l1.3-1.2 2.4 2-1.1 2.3C4.6 10.6 1.4 7.4.5 2.6z"/></svg>
        (403)871-2964
      </p>
      <p class="contact__row">
        <svg class="contact__icon" viewBox="0 0 12 12" aria-hidden="true"><path d="M0 2h12v8H0zm1 1l5 3.5L11 3z" fill-rule="evenodd"/></svg>
        info@shinebarn.com
      </p>
    </div>
  </section>

  <section class="card card--back" aria-label="Business card back">
    <div class="back__brand">
      <svg class="back__mark" viewBox="0 0 110 110" aria-hidden="true">
        <circle cx="55" cy="55" r="49" fill="none" stroke="var(--brand-red)" stroke-width="7"/>
      </svg>
      <p class="back__name">SHINE BARN AUTO CARE</p>
    </div>
    <div class="services">
      <h2 class="services__title">COMPLETE INTERIOR &amp; EXTERIOR DETAIL</h2>
      <p class="services__line">Paint correction &amp; Protection<span class="services__dot">•</span>Ceramic coating</p>
      <p class="services__line">Trim restore<span class="services__dot">•</span>Auto carpet &amp; Seat cleaning</p>
    </div>
  </section>

</body>
</html>
```